Elegant and modern Wedding Photography brochure

My existing brochure (attached) needs a major facelift. This is one of the main selling tools - it gets emailed to my clients when they make an equiry on what packages i offer and it is printed out and walked through at our first meeting. This brochure is as critical as my website - it needs to sing!

I'm looking for an eye-catching design that says:
Elegant
Modern
Clean
Crisp
Not cutesy or lovey-dovey thanks - we are more sophisticated and professional than that.

Update images to some of the latest weddings I've shot also. Let me know files and resolution you need. I've enabled right-click to download images on my site for a limited time. Please note that I retain copyright and will pursue any breeches.

Http://www.clarapennock.com/Melbourne-wedding-photography
Updates

Thanks for all of your designs! Will take a few days to decide.

Target Market(s)

Australian Women aged 24-44

Industry/Entity Type

Wedding

Font styles to use
Other font styles liked:
• Century Gothic

Requirements
Must have
• Easy to print - does not have to be 6 A4 pages like the existing brochure
Nice to have
• Some full page images - The photos are supposed to be the hero here :-)
Should not have
• Not cutesy or lovey-dovey thanks - we are more sophisticated and professional than that.

No black backgrounds, I prefer a white thanks

No images in organic shaped boxes (like the rectangles in the logo - no thanks).
Keep the lines straight and sharp

```html
<!DOCTYPE html>
<html lang="en">
<head>
<meta charset="utf-8">
<title>Clara's approach – brochure spread</title>
<link rel="stylesheet" href="https://fonts.googleapis.com/css2?family=Questrial&display=swap">
<style>
  :root {
    --canvas: #ececea;
    --paper: #fefefe;
    --plum: #8e2383;
    --spine: #9a4c9a;
    --ink: #4f4f4f;
    --photo-mono-light: #d9d9d9;
    --photo-mono-dark: #6b6b6b;
    --photo-willow: #8a8f4a;
    --photo-shade: #4b4a2c;
  }
  * { margin: 0; padding: 0; box-sizing: border-box; }
  html, body { width: 1200px; height: 900px; overflow: hidden; }
  body {
    background: var(--canvas);
    font-family: "Questrial", "Century Gothic", sans-serif;
    color: var(--ink);
    position: relative;
  }
  .spread { position: absolute; left: 42px; top: 62px; width: 1111px; height: 788px; }
  .page { position: absolute; top: 0; height: 788px; background: var(--paper); overflow: hidden; }
  .page--left { left: 0; width: 555px; }
  .page--right { left: 566px; width: 545px; }
  .spine { position: absolute; left: 555px; top: 0; width: 11px; height: 788px; background: var(--spine); }

  .title {
    position: absolute; left: 46px; top: 86px;
    font-size: 32px; line-height: 30px; font-weight: 400; color: var(--plum);
  }
  .tagline {
    position: absolute; left: 46px; top: 155px;
    font-size: 21px; font-style: italic; color: var(--plum);
  }
  .column { position: absolute; font-size: 15px; line-height: 21.2px; letter-spacing: 0.1px; }
  .column h2 {
    font-size: 16px; font-weight: 400; color: var(--plum);
    text-transform: uppercase; line-height: 21px;
  }
  .column p + h2 { margin-top: 8px; }
  .column .gap { margin-top: 27px; }

  .col-a { left: 46px; top: 212px; width: 228px; }
  .col-b { left: 285px; top: 427px; width: 225px; }
  .col-c { left: 36px; top: 42px; width: 220px; }
  .col-d { left: 274px; top: 50px; width: 220px; }

  .photo-bride {
    position: absolute; left: 285px; top: 46px; width: 222px; height: 369px;
    background: linear-gradient(180deg, var(--photo-mono-dark) 0%, var(--photo-mono-light) 45%, #a9a9a9 100%);
  }
  .photo-couple {
    position: absolute; left: 0; top: 271px; width: 545px; height: 517px;
    background: linear-gradient(160deg, var(--photo-willow) 0%, #6f7038 45%, var(--photo-shade) 80%, #3a352a 100%);
  }
  .folio { position: absolute; font-size: 12px; color: var(--plum); top: 755px; }
  .folio--left { left: 273px; }
  .folio--right { left: 265px; color: #d9cfd6; }
</style>
</head>
<body>
  <main class="spread">
    <section class="page page--left">
      <h1 class="title">Clara's<br>approach…</h1>
      <p class="tagline">Enjoy your special day!</p>

      <div class="column col-a">
        <h2>Style &amp; Approach</h2>
        <p>Clara can observe and capture your wedding day in the background, quickly and quietly taking photojournalistic pictures rather than directing it if you prefer. Or she can confidently play the role of Art Director and instruct beautiful poses. Either way, what is most important is that her clients are relaxed and having a really great time on their wedding day!</p>
        <h2>Formal Photography</h2>
        <p>Many of Clara's clients book her because of the easy-going approach she has. They can get on with having a great time on their day without worrying about formal photography. However, there are occasions when clients do want formal family pictures, and</p>
      </div>

      <div class="photo-bride" role="img" aria-label="Black and white portrait of a bride in a veil holding a rose bouquet"></div>

      <div class="column col-b">
        <p>Clara is more than happy to accommodate their requests. In order to keep the disruption on the day to a minimum, we recommend that Clara photographs no more than 6 groups, and a select number of the special couple.</p>
        <h2 class="gap">Image Presentation</h2>
        <p>The most professional way of presenting clients with their photographs is in an elegantly designed photo book.</p>
      </div>

      <span class="folio folio--left">2</span>
    </section>

    <div class="spine"></div>

    <section class="page page--right">
      <div class="column col-c">
        <p>Clara's clients only pay one fixed price for the photography, regardless of how many images taken. There are no hard sell procedures to go through, and the completed book is prepared within 2-6 weeks after the wedding day.</p>
      </div>
      <div class="column col-d">
        <h2>Time of Year</h2>
        <p>Signature pictures can be taken on overcast days or winter months. Don't worry if the sky is not perfectly blue. In the end, regardless of the weather – it's the timeless mood of the day that Clara strives to capture.</p>
      </div>

      <div class="photo-couple" role="img" aria-label="Colour photograph of a bride and groom standing beside a fallen log under willow trees"></div>
      <span class="folio folio--right">3</span>
    </section>
  </main>
</body>
</html>
```